Vor Business Card

we need a business card for flooring business called Vor Flooring, the design should be black and white. we have 2 locations

Elmridge Showroom
274 Kellaway Road,
Elmridge VIC 3148

Ashvale Showroom
592 Tarrant Hwy,
Ashvale VIC 3187

email : sales@vorflooring.com.au
(03) 9517 2643

Please inform we sell , Laminate, Hybrid, Timber, carpet and commercial flooring

```html
<!DOCTYPE html>
<html lang="en">
<head>
<meta charset="utf-8">
<title>Vor Flooring – Business Card</title>
<link href="https://fonts.googleapis.com/css2?family=Arimo:wght@400;700&display=swap" rel="stylesheet">
<style>
  :root {
    --canvas: #d9d9d9;
    --card-light: #ffffff;
    --card-dark: #333333;
    --ink: #2b2b2b;
    --ink-soft: #8a8a8a;
    --rule: #555555;
    --band-text: #ffffff;
  }
  * { margin: 0; padding: 0; box-sizing: border-box; }
  html, body {
    width: 1200px; height: 801px; overflow: hidden;
    background: var(--canvas);
    font-family: "Arimo", Arial, sans-serif;
    color: var(--ink);
  }
  .canvas {
    position: relative; width: 1200px; height: 801px;
    display: flex; align-items: center; justify-content: center; gap: 50px;
  }
  .card {
    position: relative; width: 540px; height: 330px;
    border-radius: 26px; overflow: hidden;
    box-shadow: 0 10px 28px rgba(0,0,0,0.18);
  }

  /* Front */
  .card--front { background: var(--card-light); }
  .holder { position: absolute; left: 40px; top: 40px; }
  .holder__name { font-weight: 700; font-size: 20px; letter-spacing: 0.5px; }
  .holder__role { font-size: 15px; color: var(--ink-soft); margin-top: 2px; }

  .brand {
    position: absolute; right: 38px; top: 42px;
    display: flex; align-items: center; gap: 12px;
  }
  .brand__dot { width: 14px; height: 14px; border-radius: 50%; background: var(--ink); }
  .brand__name { font-size: 34px; font-weight: 400; color: var(--ink); letter-spacing: 1px; }

  .divider {
    position: absolute; left: 40px; right: 38px; top: 150px;
    height: 1px; background: var(--rule);
  }

  .contact { position: absolute; left: 40px; top: 164px; font-size: 14px; color: var(--ink-soft); }
  .contact__row { display: flex; align-items: center; gap: 8px; line-height: 20px; }
  .contact__row svg { width: 13px; height: 13px; }
  .contact__rule { width: 200px; height: 1px; background: var(--rule); margin: 7px 0 6px; }

  .showroom { font-size: 14px; color: var(--ink-soft); line-height: 18px; }
  .showroom__title { font-weight: 700; color: var(--ink); }
  .showroom--east { position: absolute; right: 38px; top: 164px; text-align: left; width: 180px; }

  .band-rule {
    position: absolute; left: 0; right: 0; bottom: 42px;
    height: 1px; background: var(--rule);
  }
  .services-band {
    position: absolute; left: 0; right: 0; bottom: 0; height: 36px;
    background: var(--card-dark); color: var(--band-text);
    display: flex; align-items: center; justify-content: center;
    font-size: 15px; letter-spacing: 0.3px; gap: 6px;
  }

  /* Back */
  .card--back { background: var(--card-dark); display: flex; align-items: center; justify-content: center; }
  .back-brand { display: flex; align-items: center; gap: 18px; }
  .back-brand__dot { width: 22px; height: 22px; border-radius: 50%; background: var(--band-text); }
  .back-brand__name { font-size: 50px; font-weight: 400; color: var(--band-text); letter-spacing: 2px; }
</style>
</head>
<body>
<main class="canvas">

  <section class="card card--front">
    <div class="holder">
      <p class="holder__name">MARCUS HALE</p>
      <p class="holder__role">Manager</p>
    </div>

    <div class="brand">
      <span class="brand__dot"></span>
      <span class="brand__name">Vor Flooring</span>
    </div>

    <div class="divider"></div>

    <div class="contact">
      <p class="contact__row">
        <svg viewBox="0 0 16 16" aria-hidden="true"><path d="M3 1.5l3 .5 1 3.5-2 1.2a9 9 0 0 0 4.3 4.3l1.2-2 3.5 1 .5 3-2 2C6.5 15 1 9.5 1 3.5z" fill="var(--ink)"/></svg>
        (03) 9517 2643
      </p>
      <p class="contact__row">
        <svg viewBox="0 0 16 16" aria-hidden="true"><rect x="1" y="3" width="14" height="10" fill="none" stroke="var(--ink)" stroke-width="1.4"/><path d="M1 3l7 6 7-6" fill="none" stroke="var(--ink)" stroke-width="1.4"/></svg>
        sales@vorflooring.com.au
      </p>
      <div class="contact__rule"></div>
      <div class="showroom">
        <p class="showroom__title">Elmridge Showroom</p>
        <p>274 Kellaway Road,</p>
        <p>Elmridge VIC 3148</p>
      </div>
    </div>

    <div class="showroom showroom--east">
      <p class="showroom__title">Ashvale Showroom</p>
      <p>592 Tarrant Hwy,</p>
      <p>Ashvale VIC 3187</p>
    </div>

    <div class="band-rule"></div>
    <div class="services-band">
      <span>• Laminate</span><span>• Hybrid</span><span>• Timber</span><span>• carpet</span><span>• commercial flooring</span>
    </div>
  </section>

  <section class="card card--back">
    <div class="back-brand">
      <span class="back-brand__dot"></span>
      <span class="back-brand__name">Vor Flooring</span>
    </div>
  </section>

</main>
</body>
</html>
```